Green Logistics / Last Mile Delivery Firm needs cool one-page website

FYI - We do have a detailed brief in the uploaded files section below
COMPANY
We recently launched the company Brook Logistics which is a pioneer in urban green logistics and provides zero-emissions last mile delivery services (i.e. delivery of parcels with delivery vans to the doorstep of households) for its logistics and retail clients.
We take on urban parcel delivery for our clients with a 100% electric commercial vehicles fleet, fair and sustainable working conditions for our employees and an unparalleled professional and customer-focused mindset.
WEBSITE
In the detailed brief, we have provided examples to emulate. We need the design + coding of the website. Website needs to be friendly/optimized for and should open swiftly on both Android & iOS.
In general, the website should convey
- green mission of the company
- sustainability (good working conditions, focus on employees)
- customer orientation
- professionalism
DESIGN
In the detailed brief, we have provided designs to emulate.
Color design: we do have a logo which features 2 green colors (one lighter and one darker color tone). However, the colors on the website do not necessarily need to follow these 2 colors exactly as we are able to switch the logo colors.
Imagery: should reflect maybe 50% green/leaf/tree , 25% customer and employee orientation, and 25% logistics (here it's important that it is the last mile delivery, i.e. delivery with delivery vans to the doorstep of households)
Coding

```html
<!DOCTYPE html>
<html lang="en">
<head>
<meta charset="UTF-8">
<title>Brook Logistics</title>
<link href="https://fonts.googleapis.com/css2?family=Montserrat:wght@500;600;700&display=swap" rel="stylesheet">
<style>
  :root {
    --page-bg: #ffffff;
    --hero-dark: #1b3226;
    --hero-mid: #2b4a38;
    --hero-light: #3c5e48;
    --overlay: rgba(14, 30, 22, 0.55);
    --brand-green: #1f9e4a;
    --text-light: #ffffff;
    --arrow-grey: #9aa39e;
  }
  * { margin: 0; padding: 0; box-sizing: border-box; }
  html, body {
    width: 1200px; height: 1200px; overflow: hidden;
    background: var(--page-bg);
    font-family: "Montserrat", Arial, sans-serif;
  }
  .hero {
    position: absolute; left: 14px; top: 319px;
    width: 1169px; height: 559px; overflow: hidden;
  }
  .hero-photo {
    position: absolute; inset: 0;
    background:
      radial-gradient(ellipse at 68% 55%, var(--hero-light) 0%, transparent 45%),
      linear-gradient(120deg, var(--hero-dark) 0%, var(--hero-mid) 55%, var(--hero-dark) 100%);
  }
  .hero-overlay { position: absolute; inset: 0; background: var(--overlay); }
  .brand {
    position: absolute; left: 110px; top: 38px;
    display: flex; align-items: center; gap: 10px;
    text-decoration: none;
  }
  .brand-dot { width: 22px; height: 22px; border-radius: 50%; background: var(--brand-green); }
  .brand-name {
    color: var(--text-light); font-weight: 700; font-size: 16px;
  }
  .main-nav {
    position: absolute; left: 531px; top: 41px;
    display: flex; gap: 34px; list-style: none;
  }
  .main-nav a {
    color: var(--text-light); text-decoration: none;
    font-size: 12px; font-weight: 700; text-transform: uppercase;
    display: inline-block; padding-bottom: 5px;
  }
  .main-nav a.is-active { border-bottom: 2px solid var(--brand-green); }
  .lang-caret { font-size: 10px; margin-left: 3px; }
  .hero-title {
    position: absolute; left: 208px; top: 212px;
    color: var(--text-light); font-weight: 700;
    font-size: 42px; line-height: 52px; white-space: nowrap;
  }
  .cta {
    position: absolute; left: 209px; top: 341px;
    width: 173px; height: 48px; border-radius: 24px;
    background: var(--brand-green); color: var(--text-light);
    font-size: 13px; font-weight: 600; text-transform: uppercase;
    display: flex; align-items: center; justify-content: center;
    text-decoration: none;
  }
  .slider-arrow {
    position: absolute; top: 283px; width: 52px; height: 52px;
    border-radius: 50%; display: flex; align-items: center; justify-content: center;
  }
  .slider-arrow--prev { left: 32px; background: var(--arrow-grey); }
  .slider-arrow--next { left: 1086px; background: var(--text-light); }
  .scroll-hint { position: absolute; left: 575px; top: 508px; }
</style>
</head>
<body>
  <section class="hero">
    <div class="hero-photo" role="img" aria-label="Cupped hands holding soil with a young green seedling, dark green foliage behind"></div>
    <div class="hero-overlay"></div>

    <a class="brand" href="#">
      <span class="brand-dot"></span>
      <span class="brand-name">Brook Logistics</span>
    </a>

    <ul class="main-nav">
      <li><a class="is-active" href="#">Home</a></li>
      <li><a href="#">About</a></li>
      <li><a href="#">Services</a></li>
      <li><a href="#">Careers</a></li>
      <li><a href="#">Contact</a></li>
      <li><a href="#">English<span class="lang-caret">▼</span></a></li>
    </ul>

    <h1 class="hero-title">Operating the business in<br>a sustainable way</h1>
    <a class="cta" href="#">Get Started</a>

    <a class="slider-arrow slider-arrow--prev" href="#" aria-label="Previous slide">
      <svg width="16" height="16" viewBox="0 0 16 16"><path d="M10 3 L5 8 L10 13" fill="none" stroke="#2a3530" stroke-width="2.6" stroke-linecap="round" stroke-linejoin="round"/></svg>
    </a>
    <a class="slider-arrow slider-arrow--next" href="#" aria-label="Next slide">
      <svg width="16" height="16" viewBox="0 0 16 16"><path d="M6 3 L11 8 L6 13" fill="none" stroke="#1b2a22" stroke-width="2.6" stroke-linecap="round" stroke-linejoin="round"/></svg>
    </a>

    <svg class="scroll-hint" width="22" height="24" viewBox="0 0 22 24" aria-label="Scroll down">
      <path d="M4 4 L11 11 L18 4 M4 12 L11 19 L18 12" fill="none" stroke="#ffffff" stroke-width="2.4" stroke-linecap="round" stroke-linejoin="round"/>
    </svg>
  </section>
</body>
</html>
```